A Postcard Design for a Vintage/Handcrafted Fair/Event called "The Willow Gate Bazaar"

What is The Willow Gate Bazaar? It’s an indoor/outdoor Market with the feel of a vintage/village fair (like mini shops) with over 25 handpicked vendors. For example: They could be selling…Vintage, repurposed, chippy, rusty, faded, patina, furniture, antique, jewelry, Spring Décor, architectural, outdoor furnishing, garden art, handcrafted goods. The Setting again is indoor/outdoor. Outdoor is under covered tents. Indoor is in 2 pole sheds/barn. The surrounding around these tents and pole sheds are lots of woods and hay/corn fields. Truly out in the country.

Sponsored by “A Bit RMV”.
FB: pagebook.example/abitrmv
E-Mail: abitrmv@mailnest.example

Date of Event:
Friday, April 28th 9am – 7pm
Saturday, April 29th 9am – 5pm

Address of the Event:
48317 506th Ave SE
Elk River, MN 55330

This event is FREE of charge.

Although I’m open to any and all creative ideas I would appreciate if you can keep to the “Vintage/Rustic” theme (this is important…vintage like – very important). I want potential customers to look at this postcard and say “this looks fun we should go” just based off your design. Your design should be “Spring” as well. This event is in the Spring time.

The only idea I have that I thought might be a good catch would be using a swing somehow in the design and perhaps saying something like…”Swing into Spring as your browse row after row of marvelous vintage and creative handmade goods from over 25 vendors.” (This could be put on the back of the postcard if needed. Keeping the front of the postcard simple and eye catching with the name of the event (The Willow Gate Bazaar) and the dates and address. THINK SPRING though when you are designing.

Again, I’m very open to all of your creative ideas and your vision you see based on my description. You do not need to use the “swing idea” if your creative brain takes you a different direction.

Other options I put in pictures to give you some ideas of what I liked. These again are just ideas. I am open to your creative ideas. I like old bikes, old windows, old barns, vintage trucks, rope swings, vintage suitcases...I even saw a beautiful big tree that would be great as a back drop and a vintage sofa under it....or a spring/garden vignette. Banners and Bunting is vintage like and acceptable if you want. I like old barns as well. Again the setting is in pole sheds with lots of woods and fields around. Hope this will get your creative juices flowing :). lol. I'm open to all your ideas. Thank you so much for helping me creative my postcard.

Target Market(s)

The General Public

Industry/Entity Type

Event

Requirements
Must have
• Event Name: The Willow Gate Bazaar
• Sponsored by “A Bit RMV”.
• FB: pagebook.example/abitrmv
• E-Mail: abitrmv@mailnest.example
• Date of Event:
• Friday, April 28th 9am – 7pm
• Saturday, April 29th 9am – 5pm
• Address of the Event:
• 48317 506th Ave SE
• Elk River, MN 55330

```html
<!DOCTYPE html>
<html lang="en">
<head>
<meta charset="utf-8">
<title>The Willow Gate Bazaar – Postcard Back</title>
<link href="https://fonts.googleapis.com/css2?family=Questrial&family=Poppins:wght@600&display=swap" rel="stylesheet">
<style>
  :root {
    --paper: #faf6ec;
    --bar: #4a4a4a;
    --bar-text: #ffffff;
    --blush: #f7a5a2;
    --rose: #f5888d;
    --peach: #fdd3b4;
    --mint: #a9e6d3;
    --sage: #dcedc6;
    --bark: #6b4a38;
  }
  * { margin: 0; padding: 0; box-sizing: border-box; }
  html, body { width: 1200px; height: 1000px; overflow: hidden; background: var(--paper); }
  .postcard {
    position: relative;
    width: 1200px;
    height: 1000px;
    background: var(--paper);
    font-family: "Questrial", sans-serif;
    color: var(--blush);
    overflow: hidden;
  }
  .side-label {
    position: absolute; top: 0; left: 0;
    width: 1200px; height: 80px;
    background: var(--bar);
    color: var(--bar-text);
    font-family: "Poppins", sans-serif;
    font-weight: 600;
    font-size: 40px;
    line-height: 86px;
    text-align: center;
  }
  .keepsake {
    position: absolute;
    border-radius: 40% 40% 30% 30%;
  }
  .keepsake--bottle { left: -10px; top: 95px; width: 95px; height: 145px; background: var(--rose); transform: rotate(-35deg); }
  .keepsake--teapot { left: -20px; top: 295px; width: 115px; height: 140px; background: var(--peach); }
  .keepsake--vase { left: -15px; top: 530px; width: 95px; height: 180px; background: var(--mint); }
  .keepsake--lamp { left: -10px; top: 745px; width: 165px; height: 270px; background: var(--rose); border-radius: 30% 30% 10% 10%; }
  .keepsake--chandelier { left: 1060px; top: 80px; width: 150px; height: 135px; background: var(--peach); border-radius: 20%; }
  .keepsake--desk-lamp { left: 1090px; top: 285px; width: 125px; height: 115px; background: var(--mint); }
  .keepsake--kettle { left: 1095px; top: 540px; width: 120px; height: 180px; background: var(--rose); }
  .keepsake--table-lamp { left: 1020px; top: 740px; width: 190px; height: 270px; background: var(--sage); border-radius: 25% 25% 10% 10%; }

  .event-name {
    position: absolute; top: 215px; left: 0; width: 1200px;
    text-align: center;
    font-size: 84px;
    line-height: 1.1;
    color: var(--blush);
  }
  .invitation {
    position: absolute; top: 452px; left: 0; width: 1200px;
    text-align: center;
    font-size: 40px;
    line-height: 55px;
    color: var(--blush);
  }
  .sponsor {
    position: absolute; top: 690px; left: 352px;
    display: flex; align-items: center; gap: 34px;
  }
  .sponsor__label { font-size: 36px; color: var(--blush); }
  .sponsor__name {
    display: flex; align-items: center; gap: 14px;
    font-size: 34px; color: var(--bark);
  }
  .sponsor__dot { width: 26px; height: 26px; border-radius: 50%; background: var(--bark); }
  .contact {
    position: absolute; top: 868px; left: 0; width: 1200px;
    text-align: center;
    font-size: 30px;
    line-height: 48px;
    color: var(--blush);
  }
</style>
</head>
<body>
<main class="postcard">
  <header class="side-label">BACK</header>

  <div class="keepsake keepsake--bottle" role="img" aria-label="Vintage bottle silhouette"></div>
  <div class="keepsake keepsake--teapot" role="img" aria-label="Vintage teapot silhouette"></div>
  <div class="keepsake keepsake--vase" role="img" aria-label="Vintage pitcher silhouette"></div>
  <div class="keepsake keepsake--lamp" role="img" aria-label="Vintage lamp silhouette"></div>
  <div class="keepsake keepsake--chandelier" role="img" aria-label="Vintage chandelier silhouette"></div>
  <div class="keepsake keepsake--desk-lamp" role="img" aria-label="Vintage desk lamp silhouette"></div>
  <div class="keepsake keepsake--kettle" role="img" aria-label="Vintage kettle silhouette"></div>
  <div class="keepsake keepsake--table-lamp" role="img" aria-label="Vintage table lamp silhouette"></div>

  <h1 class="event-name">The Willow Gate Bazaar</h1>

  <p class="invitation">
    Swing into Spring as you browse row after row of<br>
    marvelous vintage and creative handmade goods<br>
    from over 25 vendors!
  </p>

  <div class="sponsor">
    <span class="sponsor__label">Sponsored by:</span>
    <span class="sponsor__name"><span class="sponsor__dot"></span>A Bit RMV</span>
  </div>

  <p class="contact">
    FB: pagebook.example/abitrmv<br>
    e-mail: abitrmv@mailnest.example
  </p>
</main>
</body>
</html>
```